Now Leasing Banner

Looking for a banner that says the following information approx 4' x 30'

Now Leasing Maplewood Terrace 925-318-6054

Target Market(s)

Drive by traffic

Industry/Entity Type

Residential property management

Requirements
Must have
• Clear and readable from a distance

```html
<!DOCTYPE html>
<html lang="en">
<head>
<meta charset="utf-8">
<title>Now Leasing Banner – Maplewood Terrace</title>
<link rel="stylesheet" href="https://fonts.googleapis.com/css2?family=Anton&family=League+Spartan:wght@700&display=swap">
<style>
  :root {
    --page-bg: #ffffff;
    --navy-deep: #00103f;
    --navy-mid: #1f3672;
    --sky-blue: #3292d1;
    --charcoal: #2c2e2e;
    --charcoal-light: #353838;
    --white: #ffffff;
    --cyan: #2ec4f1;
    --red: #ed1c24;
    --silver-dark: #b9babc;
    --silver-light: #f4f4f4;
  }
  * { margin: 0; padding: 0; box-sizing: border-box; }
  html, body {
    width: 1200px;
    height: 685px;
    overflow: hidden;
    background: var(--page-bg);
  }
  .sheet {
    position: relative;
    width: 1200px;
    height: 685px;
  }
  .banner {
    position: absolute;
    left: 39px;
    width: 1122px;
    height: 150px;
    overflow: hidden;
  }
  .banner--blue {
    top: 41px;
    background: linear-gradient(90deg, var(--navy-deep) 0%, var(--navy-deep) 25%, var(--navy-mid) 50%, var(--sky-blue) 72%, var(--sky-blue) 100%);
  }
  .banner--red-silver { top: 262px; }
  .banner--cyan { top: 484px; }
  .banner--red-silver,
  .banner--cyan {
    background: radial-gradient(ellipse at 55% 40%, var(--charcoal-light) 0%, var(--charcoal) 70%);
  }
  .headline {
    position: absolute;
    left: 34px;
    top: 22px;
    font-family: "Anton", "Impact", sans-serif;
    font-size: 103px;
    line-height: 1;
    letter-spacing: 0.5px;
    white-space: nowrap;
    text-transform: uppercase;
  }
  .headline__now { color: var(--white); }
  .headline__leasing { color: var(--cyan); }
  .banner--red-silver .headline__now {
    color: var(--red);
    text-shadow: 4px 5px 6px rgba(0,0,0,0.55);
  }
  .banner--red-silver .headline__leasing {
    background: linear-gradient(90deg, var(--silver-dark) 0%, var(--silver-light) 60%, var(--white) 100%);
    -webkit-background-clip: text;
    background-clip: text;
    color: transparent;
    filter: drop-shadow(4px 5px 5px rgba(0,0,0,0.55));
  }
  .contact {
    position: absolute;
    left: 578px;
    top: 26px;
    right: 0;
    color: var(--white);
    font-family: "League Spartan", "Montserrat", sans-serif;
    font-weight: 700;
  }
  .contact__name {
    font-size: 36px;
    line-height: 1;
    letter-spacing: 0.5px;
    text-transform: uppercase;
    white-space: nowrap;
  }
  .contact__rule {
    display: block;
    height: 5px;
    margin-top: 17px;
    background: var(--white);
    border-radius: 3px 0 0 3px;
  }
  .contact__phone {
    margin-top: 14px;
    font-size: 37px;
    line-height: 1;
    white-space: nowrap;
  }
</style>
</head>
<body>
  <main class="sheet">
    <section class="banner banner--blue">
      <h1 class="headline"><span class="headline__now">Now</span> <span class="headline__leasing">Leasing</span></h1>
      <div class="contact">
        <p class="contact__name">Maplewood Terrace</p>
        <span class="contact__rule"></span>
        <p class="contact__phone">925-318-6054</p>
      </div>
    </section>

    <section class="banner banner--red-silver" role="img" aria-label="Now Leasing banner on dark textured concrete background">
      <h2 class="headline"><span class="headline__now">Now</span> <span class="headline__leasing">Leasing</span></h2>
      <div class="contact">
        <p class="contact__name">Maplewood Terrace</p>
        <span class="contact__rule"></span>
        <p class="contact__phone">925-318-6054</p>
      </div>
    </section>

    <section class="banner banner--cyan" role="img" aria-label="Now Leasing banner on dark textured concrete background">
      <h2 class="headline"><span class="headline__now">Now</span> <span class="headline__leasing">Leasing</span></h2>
      <div class="contact">
        <p class="contact__name">Maplewood Terrace</p>
        <span class="contact__rule"></span>
        <p class="contact__phone">925-318-6054</p>
      </div>
    </section>
  </main>
</body>
</html>
```